Post it Note design

POST-IT NOTE DESIGN (CONTENT)
Size recommended: 4x6 for handwriting space.
Header (Bold):
Lighting Issue Detected on Your Property
Sub-header:
During our routine night inspection, we noted the following item(s):
Checkbox List:
⬜ Building Lights Out
⬜ Pole Lights Out
⬜ Sign Not Illuminated
⬜ Other ________________________
Action Line:
We can provide a quote or dispatch service right away.
Area for notes
Contact Block (Bold & Centered):
Brovane Fixture Inc.
Service@BrovaneFixture.com
www.BrovaneFixture.com
877-514-0862
Industry/Entity Type
Electrical lighting
Colors
Designer to choose colors to be used in the design.
Look and feel
Each slider illustrates characteristics of the customer's brand and the style your logo design should communicate.

```html
<!DOCTYPE html>
<html lang="en">
<head>
<meta charset="UTF-8">
<title>Brovane Fixture Inc. – Lighting Issue Notice</title>
<link href="https://fonts.googleapis.com/css2?family=Montserrat:ital,wght@0,400;0,500;0,700;0,800;0,900;1,500;1,800&display=swap" rel="stylesheet">
<style>
  :root {
    --page-bg: #d9d9d9;
    --navy: #12238a;
    --navy-deep: #0d1f78;
    --royal: #1f46e6;
    --royal-bright: #1340ee;
    --red: #ea0f1f;
    --white: #ffffff;
    --ink: #262626;
    --rule: #3a3a3a;
    --glow: #d9b24a;
  }
  * { margin: 0; padding: 0; box-sizing: border-box; }
  html, body {
    width: 929px; height: 1200px; overflow: hidden;
    background: var(--page-bg);
    font-family: "Montserrat", sans-serif;
  }
  .canvas { position: relative; width: 929px; height: 1200px; }

  .card { position: absolute; left: 94px; width: 742px; height: 495px; overflow: hidden; }

  /* Front */
  .card-front {
    top: 87px;
    background: radial-gradient(circle at 0% 0%, #3b63e0 0%, var(--navy) 28%, var(--navy-deep) 100%);
    color: var(--white);
  }
  .brand-name {
    position: absolute; left: 60px; top: 40px; width: 275px;
    text-align: center; color: var(--red);
    font-weight: 800; font-size: 34px; line-height: 1.05; letter-spacing: 0.5px;
    text-transform: uppercase;
  }
  .issue-tag {
    position: absolute; left: 51px; top: 167px; width: 292px; height: 56px;
    background: var(--royal); border-radius: 8px 0 8px 0;
    display: flex; align-items: center; justify-content: center;
    font-weight: 800; font-size: 30px; letter-spacing: 0.2px;
  }
  .issue-line {
    position: absolute; left: 51px; top: 229px; width: 292px; text-align: center;
    font-weight: 800; font-size: 26px; letter-spacing: 0.2px;
  }
  .issue-emphasis {
    position: absolute; left: 51px; top: 258px; width: 292px; text-align: center;
    font-weight: 900; font-size: 52px; color: var(--red); letter-spacing: -0.5px; line-height: 1.1;
  }
  .inspection-note {
    position: absolute; left: 50px; top: 332px; width: 320px;
    font-style: italic; font-weight: 500; font-size: 16.5px; line-height: 1.3;
  }
  .checklist-title {
    position: absolute; left: 50px; top: 385px;
    font-weight: 500; font-size: 20px;
  }
  .checklist-underline { position: absolute; left: 50px; top: 408px; }
  .checklist {
    position: absolute; left: 51px; top: 425px; width: 360px;
    display: grid; grid-template-columns: 187px 1fr; row-gap: 7px;
    list-style: none; font-size: 15px; font-weight: 500;
  }
  .checklist li { display: flex; align-items: center; gap: 9px; }
  .checkbox { width: 12px; height: 12px; border: 1px solid #c9d2f5; display: inline-block; }

  .scene-glow {
    position: absolute; right: 0; top: 0; width: 330px; height: 495px;
    background: radial-gradient(ellipse at 65% 25%, rgba(217,178,74,0.55) 0%, rgba(217,178,74,0.15) 35%, transparent 65%);
  }
  .technician-photo {
    position: absolute; left: 440px; top: 135px; width: 271px; height: 360px;
    border-radius: 140px 0 0 0;
    background: linear-gradient(180deg, var(--royal-bright) 0%, #2a4c9a 55%, #1b2f6e 100%);
  }

  /* Back */
  .card-back { top: 618px; background: var(--white); }
  .back-band {
    position: absolute; left: 0; top: 0; width: 742px; height: 96px;
    background: linear-gradient(180deg, var(--navy) 0%, #2a3aa0 70%, rgba(255,255,255,0) 100%);
  }
  .back-band-glow {
    position: absolute; right: 0; top: 0; width: 380px; height: 96px;
    background: radial-gradient(ellipse at 60% 20%, rgba(217,178,74,0.5), transparent 70%);
  }
  .action-line {
    position: absolute; left: 47px; top: 117px; width: 260px;
    font-size: 26px; font-weight: 500; line-height: 1.15; color: var(--ink);
  }
  .action-line em { font-style: italic; font-weight: 800; color: var(--red); }
  .notes-rule { position: absolute; height: 1px; background: var(--rule); }
  .notes-rule.short { left: 331px; width: 364px; }
  .notes-rule.full { left: 43px; width: 652px; }

  .contact-phone {
    position: absolute; left: 47px; top: 420px;
    display: flex; align-items: center; gap: 16px;
    font-weight: 800; font-size: 35px; color: var(--ink); letter-spacing: -0.5px;
  }
  .contact-lines {
    position: absolute; left: 367px; top: 412px;
    list-style: none; font-size: 16.5px; font-weight: 500; color: var(--ink);
  }
  .contact-lines li { display: flex; align-items: center; gap: 16px; height: 27px; }
</style>
</head>
<body>
<div class="canvas">

  <section class="card card-front">
    <div class="scene-glow"></div>
    <div class="technician-photo" role="img" aria-label="Photo of a smiling electrician in a yellow hard hat and work shirt holding coiled cables, under glowing street lamps"></div>

    <div class="brand-name">Brovane Fixture Inc.</div>

    <div class="issue-tag">LIGHTING ISSUE</div>
    <div class="issue-line">DETECTED ON YOUR</div>
    <div class="issue-emphasis">PROPERTY</div>

    <p class="inspection-note">During our routine night inspection, we noted the following item(s):</p>

    <h2 class="checklist-title">Checklist</h2>
    <svg class="checklist-underline" width="92" height="6" viewBox="0 0 92 6" aria-hidden="true">
      <path d="M1 4 Q12 1 23 3.5 T46 3.5 T69 3.5 T91 2" fill="none" stroke="#3d6bff" stroke-width="2.2" stroke-linecap="round"/>
    </svg>
    <ul class="checklist">
      <li><span class="checkbox"></span>Building Lights Out</li>
      <li><span class="checkbox"></span>Sign Not Illuminated</li>
      <li><span class="checkbox"></span>Pole Lights Out</li>
      <li><span class="checkbox"></span>Other</li>
    </ul>
  </section>

  <section class="card card-back">
    <div class="back-band"></div>
    <div class="back-band-glow"></div>

    <p class="action-line">We can provide a <em>Quote or Dispatch Service</em> right away.</p>

    <div class="notes-rule short" style="top:126px"></div>
    <div class="notes-rule short" style="top:176px"></div>
    <div class="notes-rule full" style="top:225px"></div>
    <div class="notes-rule full" style="top:275px"></div>
    <div class="notes-rule full" style="top:324px"></div>
    <div class="notes-rule full" style="top:374px"></div>

    <div class="contact-phone">
      <svg width="22" height="22" viewBox="0 0 24 24" aria-hidden="true">
        <path d="M4 22 C2 14 8 4 20 3 L22 7 C14 8 10 13 9 20 Z" fill="var(--red)"/>
      </svg>
      877-514-0862
    </div>
    <ul class="contact-lines">
      <li>
        <svg width="15" height="16" viewBox="0 0 15 16" aria-hidden="true"><path d="M2 1 L13 8 L8 9 L11 15 L9 15.5 L6.5 10 L3 13 Z" fill="var(--red)"/></svg>
        www.BrovaneFixture.com
      </li>
      <li>
        <svg width="16" height="12" viewBox="0 0 16 12" aria-hidden="true"><rect x="0" y="0" width="16" height="12" rx="1.5" fill="var(--red)"/><path d="M1 1.5 L8 7 L15 1.5" fill="none" stroke="#fff" stroke-width="1.4"/></svg>
        Service@BrovaneFixture.com
      </li>
    </ul>
  </section>

</div>
</body>
</html>
```